Business Card Design Project

- makeup artist business card

- original and creative

- Elegant design

- Feel free to come out with cool designs but stick to being elegant and attractive

- Design relates to makeup

- includes name, occupation, contact numbers, email, website

- regular size business card

- round corner card

- double sided

- on 1 side it should just have the website name in the center " browsandblush.example "

Industry/Entity Type

Business

Requirements
Must have
• Marla Voss
Makeup Artist
USA: +1 (415)872-6410
Singapore: +65 83027715
marlavoss@browsandblush.example
www.browsandblush.example
Should not have
• nothing cartoon looking.
Pictures of makeup being grab from the internet.. Examples: eyes or lips.

```html
<!DOCTYPE html>
<html lang="en">
<head>
<meta charset="utf-8">
<title>Marla Voss – Makeup Artist Business Card</title>
<link rel="stylesheet" href="https://fonts.googleapis.com/css2?family=Herr+Von+Muellerhoff&family=Arimo:wght@400&display=swap">
<style>
  :root {
    --page: #ececec;
    --card-black: #141414;
    --card-paper: #f4f3f0;
    --ink: #111111;
    --script-light: #e9e9e9;
    --wash-teal: #9fb2ac;
    --wash-sage: #b9c2b4;
    --wash-skin: #d9c7bb;
    --wash-rose: #c9a8a4;
    --shadow: rgba(0, 0, 0, 0.18);
  }
  * { box-sizing: border-box; margin: 0; padding: 0; }
  html, body {
    width: 1200px;
    height: 1200px;
    overflow: hidden;
    background: var(--page);
  }
  .canvas {
    position: relative;
    width: 1200px;
    height: 1200px;
  }
  .card {
    position: absolute;
    left: 150px;
    width: 900px;
    height: 514px;
    border-radius: 14px;
    overflow: hidden;
    box-shadow: 0 10px 30px var(--shadow);
  }
  .card--back {
    top: 56px;
    background: var(--card-black);
    display: flex;
    align-items: center;
    justify-content: center;
  }
  .card--front {
    top: 630px;
    background: var(--card-paper);
  }
  .back-website {
    font-family: "Herr Von Muellerhoff", cursive;
    font-size: 92px;
    color: var(--script-light);
    letter-spacing: 1px;
    transform: translateY(-4px);
  }
  .portrait-area {
    position: absolute;
    left: 0;
    top: 0;
    width: 430px;
    height: 100%;
    background:
      radial-gradient(ellipse 55% 45% at 58% 42%, var(--wash-skin) 0%, rgba(217,199,187,0.6) 50%, transparent 80%),
      radial-gradient(ellipse 30% 12% at 72% 60%, var(--wash-rose) 0%, transparent 100%),
      radial-gradient(ellipse 50% 60% at 15% 30%, var(--wash-teal) 0%, transparent 75%),
      linear-gradient(180deg, var(--wash-sage) 0%, var(--wash-skin) 55%, var(--wash-sage) 100%);
    -webkit-mask-image: linear-gradient(90deg, #000 0%, #000 70%, transparent 100%);
            mask-image: linear-gradient(90deg, #000 0%, #000 70%, transparent 100%);
    opacity: 0.9;
  }
  .identity {
    position: absolute;
    left: 400px;
    top: 118px;
    width: 440px;
    text-align: right;
  }
  .identity__name {
    font-family: "Herr Von Muellerhoff", cursive;
    font-weight: 400;
    font-size: 118px;
    line-height: 1;
    color: var(--ink);
    white-space: nowrap;
  }
  .identity__role {
    font-family: "Arimo", Arial, sans-serif;
    font-size: 26px;
    letter-spacing: 1px;
    color: var(--ink);
    margin-top: -6px;
    padding-right: 18px;
  }
  .contact {
    position: absolute;
    right: 32px;
    bottom: 42px;
    list-style: none;
    text-align: right;
    font-family: "Arimo", Arial, sans-serif;
    font-size: 25px;
    line-height: 1.3;
    color: var(--ink);
  }
</style>
</head>
<body>
  <main class="canvas">
    <section class="card card--back" aria-label="Card back">
      <p class="back-website">browsandblush.example</p>
    </section>

    <section class="card card--front" aria-label="Card front">
      <div class="portrait-area" role="img" aria-label="Soft watercolour portrait illustration in teal, sage and skin tones"></div>
      <div class="identity">
        <h1 class="identity__name">Marla Voss</h1>
        <p class="identity__role">MAKEUP ARTIST</p>
      </div>
      <ul class="contact">
        <li>USA: +1 (415)872-6410</li>
        <li>Singapore: +65 83027715</li>
        <li>marlavoss@browsandblush.example</li>
        <li>www.browsandblush.example</li>
      </ul>
    </section>
  </main>
</body>
</html>
```